The Fen Bloom Organic & Natural Soaps needs a good business card

I am sorry for the lack of direction or Scope of the project. I am new at this board.
This is my scope and requirements:
Business card project:
This is related to the Label project I also opened up. (The Fen Bloom Organic & Natural Soaps is looking for label designs (along with the business card project (Contest) )
I have attached an initial draft at a logo I tried to come up with for a business card and labelling/marketing. I am hoping that you can take this logo and 'run with it' to finesse it, make it look unique and professional. I am open to new logo ideas.
I am a start up at home company making Organic and Natural Bar soaps, hand soaps, body washes.
All of my ingredients are organic or natural and will include natural essential oils, exfoliants, natural powders/colours, etc.
Some of the names are: Tandivex (feisty, energetic soap), Quill (more of a sandalwood earthy tones with a sandalwood powder exfoliant), Dusky (maybe changing this name - fresh scented), Plum Sorrel (lemongrass/ginger, exfoliants), etc....
I am attaching the cardstock I am looking at for packaging as well - this might help with the business card aspect. I was originally just looking at plain kraft paper but am receiving samples of Bern Aldry coloured kraft paper. I may still print business cards on the plain kraft though.. not sure.
If you need more information, please let me know.
Odile
I
Business Card and Labels
I have come up with a basic logo that I like. If you can finesse it and provide a great business card, that would be great.
I am starting up an at home soap business that will include luxury organic bar soaps, luxury natural olive oil bar soaps, organic hand wash, natural olive oil based body wash. I will be selling online and at shows.
please find attached my logo idea that I would like to incorporate.
I am also looking at packaging/labelling ideas for the bar soaps (prefer kraft cardstock wrap) and labels for the various body washes (natural soap) and the hand washes (organic). The hand washes will be in 250ml square bottles and the body wash will be in tapered bottles (smaller at top going to bottom).
Please let me know if you need more info!
I am also looking for packaging (label design for hand soap/body wash bottles and label design for organic/natural soaps)
This Project coincides with the business card project I also posted: there are 2 projects related - 1) business cards, 2) labels for organic hand wash, natural body wash, sticker label or design for kraft paper to package around luxury organic and natural soaps. I am not sure if a sticker would look nice or the design for the thick kraft paper.
Thank you!
Business card project:
This is related to the Label project I also opened up. (The Fen Bloom Organic & Natural Soaps is looking for label designs (along with the business card proje (Contest) )
I have attached an initial draft at a logo I tried to come up with for a business card and labelling/marketing. I am hoping that you can take this logo and 'run with it' to finesse it, make it look unique and professional.
Odile
I
Hello; I just wanted to let everyone know that if you feel that this
brand needs a different logo, I am open to ideas (if you don't think the
one I started with is ok). I am coming to the experts here!
Just to confirm also - this is related to the label/packaging project, therefore, there are 2 projects, 2 payments! :)
Cheers

```html
<!DOCTYPE html>
<html lang="en">
<head>
<meta charset="utf-8">
<title>The Fen Bloom – Soap Labels</title>
<link rel="stylesheet" href="https://fonts.googleapis.com/css2?family=Comfortaa:wght@400;500&family=Fredoka:wght@600&family=Crimson+Text:ital,wght@1,600&display=swap">
<style>
  :root {
    --board: #ffffff;
    --board-edge: #d6d6d6;
    --kraft: #a98e6c;
    --kraft-light: #b39a79;
    --kraft-dark: #9b8060;
    --band: #57402f;
    --logo: #ffffff;
    --ink: #2f2218;
    --yellow: #f3d31c;
    --blue: #2a8fcb;
    --brown: #6d4a32;
    --orange: #e8781f;
  }
  * { box-sizing: border-box; margin: 0; padding: 0; }
  html, body { width: 1200px; height: 779px; overflow: hidden; }
  body {
    background: radial-gradient(ellipse at 50% 45%, #ffffff 40%, #efefef 100%);
    position: relative;
  }
  .board {
    position: absolute; inset: 2px;
    border: 1px solid var(--board-edge);
  }
  .label {
    position: absolute;
    width: 363px; height: 255px;
    background:
      repeating-linear-gradient(0deg, rgba(0,0,0,.035) 0 1px, transparent 1px 3px),
      repeating-linear-gradient(90deg, rgba(255,255,255,.03) 0 1px, transparent 1px 3px),
      linear-gradient(160deg, var(--kraft-light), var(--kraft) 50%, var(--kraft-dark));
  }
  .label--a { left: 203px; top: 101px; }
  .label--b { left: 634px; top: 101px; }
  .label--c { left: 203px; top: 423px; }
  .label--d { left: 634px; top: 423px; }
  .brand-band {
    position: absolute; left: 0; right: 0; top: 42px; height: 85px;
    background: var(--band);
    display: flex; flex-direction: column; align-items: center; justify-content: center;
    color: var(--logo);
    font-family: "Comfortaa", sans-serif;
  }
  .brand-name { font-size: 27px; font-weight: 500; line-height: 1.1; }
  .brand-tagline { font-size: 11px; font-weight: 500; margin-top: 3px; }
  .product {
    position: absolute; left: 0; right: 0; top: 170px;
    text-align: center;
  }
  .product-name {
    font-family: "Fredoka", sans-serif;
    font-weight: 600; font-size: 31px; line-height: 1;
    -webkit-text-stroke: 5px var(--ink);
    paint-order: stroke fill;
    letter-spacing: .5px;
  }
  .product-note {
    font-family: "Crimson Text", serif;
    font-style: italic; font-weight: 600;
    font-size: 14px; color: var(--ink);
    margin-top: 5px;
  }
  .tone-yellow { color: var(--yellow); }
  .tone-blue { color: var(--blue); }
  .tone-brown { color: var(--brown); }
  .tone-orange { color: var(--orange); }
</style>
</head>
<body>
  <div class="board"></div>

  <section class="label label--a">
    <div class="brand-band"><span class="brand-name">The Fen Bloom</span><span class="brand-tagline">Organic &amp; Natural Soaps</span></div>
    <div class="product"><div class="product-name tone-yellow">Tandivex</div><div class="product-note">feisty and energetic feel</div></div>
  </section>

  <section class="label label--b">
    <div class="brand-band"><span class="brand-name">The Fen Bloom</span><span class="brand-tagline">Organic &amp; Natural Soaps</span></div>
    <div class="product"><div class="product-name tone-blue">Dusky</div><div class="product-note">fresh scented</div></div>
  </section>

  <section class="label label--c">
    <div class="brand-band"><span class="brand-name">The Fen Bloom</span><span class="brand-tagline">Organic &amp; Natural Soaps</span></div>
    <div class="product"><div class="product-name tone-brown">Quill</div><div class="product-note">sandalwood powder exfoliant</div></div>
  </section>

  <section class="label label--d">
    <div class="brand-band"><span class="brand-name">The Fen Bloom</span><span class="brand-tagline">Organic &amp; Natural Soaps</span></div>
    <div class="product"><div class="product-name tone-orange">Plum Sorrel</div><div class="product-note">lemongrass and ginger exfoliants</div></div>
  </section>
</body>
</html>
```